Update patient consent forms and contract

Objective
Redesign the existing patient contract information document to create a modern,contempory, and easy-to-understand experience for patients. The updated design should improve readability, accessibility, and overall presentation while maintaining compliance with healthcare and legal requirements.

Key Deliverables

Refreshed visual design and layout
Improved information hierarchy and readability
Modern typography and colour palette aligned with brand guidelines
Clear section headings and navigation
Print-ready and digital versions (PDF)

Include KEV Logo within patient KEV consent to treatment. Ideally this document should be portrait not landscape.
Updates

I would love a front page to be included in the document

```html
<!DOCTYPE html>
<html lang="en">
<head>
<meta charset="utf-8">
<title>KEV Orthodontic Treatment Information &amp; Consent Guide</title>
<link rel="stylesheet" href="https://fonts.googleapis.com/css2?family=Inter:wght@300;400;500;600&display=swap">
<style>
:root{
  --navy:#10294a;
  --band:#0d2747;
  --ink:#26354a;
  --muted:#5b6a7e;
  --rule:#9fb0c6;
  --tint:#eef3f9;
  --tint-line:#b9c9dc;
  --canvas:#eceef1;
  --paper:#ffffff;
  --chip:#e8edf3;
}
*{box-sizing:border-box;margin:0;padding:0}
html,body{width:800px;height:1200px;overflow:hidden}
body{background:var(--canvas);font-family:"Inter",Arial,sans-serif;color:var(--ink);position:relative}
.page{position:absolute;background:var(--paper);overflow:hidden;width:262px}
.r1{top:0;height:440px}.r2{top:446px;height:381px}.r3{top:833px;height:350px}
.c1{left:0}.c2{left:268px}.c3{left:537px}
.brand{position:absolute;left:22px;top:22px;display:flex;align-items:center;gap:5px;color:var(--muted);font-size:6.4px;line-height:1.05;font-weight:400}
.brand .dot{width:22px;height:22px;border-radius:50%;background:var(--chip);border:1px solid #c9d2dd;flex:none}
.top-rule{position:absolute;left:22px;right:22px;top:55px;height:1px;background:var(--rule)}
.footer{position:absolute;left:0;right:0;bottom:0;height:24px;background:var(--band);color:#fff;font-size:6.4px;display:flex;align-items:center;justify-content:space-between;padding:0 18px 0 20px}
.footer .url{display:flex;align-items:center;gap:4px}
.title{position:absolute;left:22px;color:var(--navy);font-weight:300;font-size:15.6px;line-height:1.25}
.body{position:absolute;left:22px;right:22px;font-size:6.3px;line-height:1.9;color:var(--ink);font-weight:400}
.body p+p{margin-top:8px}
.box{position:absolute;left:22px;right:22px;background:var(--tint);border:1px solid var(--tint-line);border-radius:5px}
/* cover */
.cover .brand{top:28px;left:22px;font-size:11px;color:var(--navy);gap:7px}
.cover .brand .dot{width:34px;height:34px}
.cover-title{position:absolute;left:22px;top:138px;font-size:24px;line-height:1.06;font-weight:400;color:var(--navy);letter-spacing:-.2px}
.cover-rule{position:absolute;left:22px;top:256px;width:147px;height:1px;background:var(--rule)}
.cover-tag{position:absolute;left:22px;top:276px;font-size:7.2px;line-height:1.7;color:var(--navy)}
.cover-art{position:absolute;left:52px;top:112px;width:210px;height:310px;background:radial-gradient(ellipse at 65% 85%,#d7dee7 0%,#eef1f5 45%,rgba(255,255,255,0) 72%)}
.cover-url{position:absolute;left:22px;bottom:16px;font-size:6.4px;color:var(--navy);display:flex;align-items:center;gap:4px}
/* toc */
.toc{position:absolute;left:22px;right:22px;top:110px;list-style:none;font-size:5.6px;color:var(--navy)}
.toc li{display:flex;align-items:baseline;height:12.3px}
.toc li.sub{padding-left:11px;color:var(--ink)}
.toc .n{width:10px}.toc li.sub .n{width:15px}
.toc .lead{flex:1;border-bottom:1px dotted #b4bfcc;margin:0 3px}
/* lists */
.ticks{list-style:none;font-size:5.9px;line-height:15px;color:var(--ink)}
.ticks li{display:flex;align-items:center;gap:6px}
.benefits{position:absolute;left:22px;right:22px;top:115px;list-style:none;font-size:7.6px;color:var(--ink)}
.benefits li{display:flex;align-items:center;gap:9px;height:26.2px}
.ic{width:17px;height:17px;border-radius:50%;background:var(--navy);display:flex;align-items:center;justify-content:center;flex:none}
.risks{position:absolute;left:32px;right:16px;list-style:none;font-size:7.6px;color:var(--ink)}
.risks li{display:flex;align-items:center;height:27.3px}
.num{width:17px;height:17px;border-radius:50%;background:var(--navy);color:#fff;font-size:7.5px;font-weight:500;display:flex;align-items:center;justify-content:center;flex:none}
.chip{width:21px;height:21px;border-radius:50%;background:var(--chip);display:flex;align-items:center;justify-content:center;margin:0 12px 0 9px;flex:none}
.mini-head{position:absolute;left:22px;top:22px;display:flex;align-items:flex-start;gap:6px}
.mini-head .dot{width:21px;height:21px;border-radius:50%;background:var(--chip);border:1px solid #c9d2dd;flex:none}
.mini-head h2{font-size:8.6px;font-weight:400;color:var(--navy);line-height:1.2;margin-top:2px}
.mini-head small{display:block;font-size:6.8px;color:var(--ink)}
h3.sub{position:absolute;left:22px;font-size:8px;font-weight:400;color:var(--navy)}
</style>
</head>
<body>
<svg width="0" height="0" style="position:absolute" aria-hidden="true">
  <symbol id="tooth" viewBox="0 0 14 18"><path d="M4.5 2.5c-2 0-3 1.8-3 4 0 3 1.2 4.2 1.6 7 .3 2 1.5 2 1.8 0 .3-2 .8-3 2.1-3s1.8 1 2.1 3c.3 2 1.5 2 1.8 0 .4-2.8 1.6-4 1.6-7 0-2.2-1-4-3-4-1.2 0-1.6.6-2.5.6S5.7 2.5 4.5 2.5z" fill="none" stroke="currentColor" stroke-width="1.2" stroke-linejoin="round"/></symbol>
  <symbol id="globe" viewBox="0 0 12 12"><g fill="none" stroke="currentColor" stroke-width="1"><circle cx="6" cy="6" r="5"/><ellipse cx="6" cy="6" rx="2.2" ry="5"/><path d="M1 6h10"/></g></symbol>
  <symbol id="tick" viewBox="0 0 10 10"><g fill="none" stroke="currentColor" stroke-width="1"><circle cx="5" cy="5" r="4"/><path d="M3 5.2l1.4 1.4L7 3.8"/></g></symbol>
</svg>

<!-- Page 1: cover -->
<section class="page r1 c1 cover">
  <div class="cover-art" role="img" aria-label="Soft illustration of a smile with braces on the upper teeth and a flowing line"></div>
  <div class="brand"><span class="dot"></span><span>Kestrel Valley<br>Orthodontics</span></div>
  <h1 class="cover-title">Orthodontic<br>Treatment<br>Information &amp;<br>Consent Guide</h1>
  <div class="cover-rule"></div>
  <p class="cover-tag">Your smile. Our specialty.<br>A partnership for lifelong oral health.</p>
  <div class="cover-url"><svg width="8" height="8"><use href="#globe"/></svg>kev.org.au</div>
</section>

<!-- Page 2: contents -->
<section class="page r1 c2">
  <div class="brand"><span class="dot"></span><span>Kestrel Valley<br>Orthodontics</span></div>
  <h2 class="title" style="top:70px">Table of Contents</h2>
  <div class="top-rule" style="top:95px"></div>
  <ol class="toc">
    <li><span class="n">1.</span>About This Guide<span class="lead"></span>03</li>
    <li><span class="n">2.</span>Orthodontic Treatment Overview<span class="lead"></span>04</li>
    <li><span class="n">3.</span>Benefits of Treatment<span class="lead"></span>05</li>
    <li><span class="n">4.</span>Risks of Orthodontic Treatment<span class="lead"></span>06</li>
    <li class="sub"><span class="n">4.1</span>Change in Tooth Colour<span class="lead"></span>07</li>
    <li class="sub"><span class="n">4.2</span>Tooth Sensitivity<span class="lead"></span>07</li>
    <li class="sub"><span class="n">4.3</span>Discomfort<span class="lead"></span>08</li>
    <li class="sub"><span class="n">4.4</span>Root Resorption<span class="lead"></span>08</li>
    <li class="sub"><span class="n">4.5</span>Decalcification (White Spots)<span class="lead"></span>09</li>
    <li class="sub"><span class="n">4.6</span>Gum Problems<span class="lead"></span>09</li>
    <li class="sub"><span class="n">4.7</span>Tooth Movement Limitations<span class="lead"></span>10</li>
    <li class="sub"><span class="n">4.8</span>Treatment Duration<span class="lead"></span>10</li>
    <li class="sub"><span class="n">4.9</span>Relapse<span class="lead"></span>11</li>
    <li class="sub"><span class="n">4.10</span>Changes to Bite<span class="lead"></span>11</li>
    <li class="sub"><span class="n">4.11</span>Need for Additional Treatment<span class="lead"></span>12</li>
    <li class="sub"><span class="n">4.12</span>Allergic Reactions<span class="lead"></span>12</li>
    <li class="sub"><span class="n">4.13</span>Appliance Breakage or Failure<span class="lead"></span>13</li>
    <li class="sub"><span class="n">4.14</span>Other Unexpected Risks<span class="lead"></span>13</li>
    <li><span class="n">5.</span>Your Responsibilities<span class="lead"></span>14</li>
    <li><span class="n">6.</span>Consent to Treatment<span class="lead"></span>15</li>
    <li><span class="n">7.</span>Payment Option Selection<span class="lead"></span>16</li>
    <li><span class="n">8.</span>Retainer Policy<span class="lead"></span>17</li>
    <li><span class="n">9.</span>Contact Information<span class="lead"></span>18</li>
  </ol>
  <footer class="footer"><span class="url"><svg width="8" height="8"><use href="#globe"/></svg>kev.org.au</span><span>02</span></footer>
</section>

<!-- Page 3: about -->
<section class="page r1 c3">
  <div class="brand"><span class="dot"></span><span>Kestrel Valley<br>Orthodontics</span></div>
  <div class="top-rule" style="top:70px"></div>
  <h2 class="title" style="top:88px">1. About This Guide</h2>
  <div class="body" style="top:128px">
    <p>This guide has been developed by Kestrel Valley Orthodontics (KEV) to help you understand orthodontic treatment, its benefits, potential risks and your role in achieving the best possible outcome.</p>
    <p>Please read this information carefully. Your orthodontist will also explain anything you do not understand and help you make an informed decision about your care.</p>
  </div>
  <div class="box" style="top:266px;height:82px;padding:14px 14px 0 36px">
    <svg style="position:absolute;left:10px;top:14px" width="18" height="18" viewBox="0 0 18 18"><circle cx="9" cy="9" r="9" fill="var(--navy)"/><rect x="8" y="7.5" width="2" height="6" fill="#fff"/><circle cx="9" cy="5" r="1.2" fill="#fff"/></svg>
    <div style="font-size:8.6px;color:var(--navy);margin-bottom:6px">Important</div>
    <div style="font-size:5.8px;line-height:2;color:var(--ink)">This document provides general information only and does not replace personalised advice from your orthodontist.</div>
  </div>
  <footer class="footer"><span class="url"><svg width="8" height="8"><use href="#globe"/></svg>kev.org.au</span><span>03</span></footer>
</section>

<!-- Page 4: overview -->
<section class="page r2 c1">
  <div class="brand" style="left:20px"><span class="dot"></span><span>Kestrel Valley<br>Orthodontics</span></div>
  <div class="top-rule" style="top:56px"></div>
  <h2 class="title" style="top:68px">2. Orthodontic<br>&nbsp;&nbsp;&nbsp;&nbsp;Treatment Overview</h2>
  <div class="body" style="top:114px">
    <p>Orthodontic treatment involves the use of appliances to gently move your teeth and jaws into a healthier, more functional and aesthetically pleasing position.</p>
    <p>Treatment may involve braces, aligners or other appliances and is tailored to your individual needs.</p>
  </div>
  <div class="box" style="top:199px;height:114px;padding:10px 0 0 47px">
    <svg style="position:absolute;left:14px;top:10px;color:var(--navy)" width="22" height="26"><use href="#tooth"/></svg>
    <div style="font-size:8.6px;color:var(--navy);margin-bottom:3px">Treatment Goals</div>
    <ul class="ticks">
      <li><svg width="6" height="6" style="color:var(--muted)"><use href="#tick"/></svg>Improve dental alignment</li>
      <li><svg width="6" height="6" style="color:var(--muted)"><use href="#tick"/></svg>Enhance facial balance</li>
      <li><svg width="6" height="6" style="color:var(--muted)"><use href="#tick"/></svg>Improve oral function</li>
      <li><svg width="6" height="6" style="color:var(--muted)"><use href="#tick"/></svg>Support long-term oral health</li>
      <li><svg width="6" height="6" style="color:var(--muted)"><use href="#tick"/></svg>Increase confidence and self-esteem</li>
    </ul>
  </div>
  <footer class="footer"><span class="url"><svg width="8" height="8"><use href="#globe"/></svg>kev.org.au</span><span>04</span></footer>
</section>

<!-- Page 5: benefits -->
<section class="page r2 c2">
  <div class="brand"><span class="dot"></span><span>Kestrel Valley<br>Orthodontics</span></div>
  <div class="top-rule" style="top:56px"></div>
  <h2 class="title" style="top:68px">3. Benefits of Treatment</h2>
  <div class="body" style="top:92px">Orthodontic treatment can provide both oral health and quality of life benefits, including:</div>
  <ul class="benefits">
    <li><span class="ic"><svg width="9" height="11" style="color:#fff"><use href="#tooth"/></svg></span>Improved appearance and smile confidence</li>
    <li><span class="ic"><svg width="9" height="11" style="color:#fff"><use href="#tooth"/></svg></span>Better chewing and speaking function</li>
    <li><span class="ic"><svg width="9" height="11" style="color:#fff"><use href="#tooth"/></svg></span>Easier cleaning and improved oral hygiene</li>
    <li><span class="ic"><svg width="9" height="11" style="color:#fff"><use href="#tooth"/></svg></span>Reduced risk of tooth decay and gum disease</li>
    <li><span class="ic"><svg width="9" height="11" style="color:#fff"><use href="#tooth"/></svg></span>Improved jaw function and comfort</li>
    <li><span class="ic"><svg width="9" height="11" style="color:#fff"><use href="#tooth"/></svg></span>Long-term stability with proper retention</li>
  </ul>
  <div class="box" style="top:302px;height:38px;border:none;padding:9px 0 0 40px;font-size:5.8px;line-height:1.9">
    <svg style="position:absolute;left:12px;top:11px" width="18" height="16" viewBox="0 0 18 16"><path d="M9 15S1 10 1 5a4 4 0 0 1 8-1 4 4 0 0 1 8 1c0 5-8 10-8 10z" fill="none" stroke="var(--navy)" stroke-width="1.2"/></svg>
    A healthy smile can benefit your overall wellbeing and quality of life.
  </div>
  <footer class="footer"><span class="url"><svg width="8" height="8"><use href="#globe"/></svg>kev.org.au</span><span>05</span></footer>
</section>

<!-- Page 6: risks intro -->
<section class="page r2 c3">
  <div class="brand"><span class="dot"></span><span>Kestrel Valley<br>Orthodontics</span></div>
  <div class="top-rule" style="top:56px"></div>
  <h2 class="title" style="top:68px">4. Risks of Orthodontic<br>Treatment</h2>
  <div class="body" style="top:114px">
    <p>Like all healthcare treatments, orthodontic treatment carries potential risks and limitations. These risks are generally uncommon and most can be managed if identified early.</p>
    <p>There are 14 key risk categories outlined below.</p>
  </div>
  <svg style="position:absolute;left:118px;top:210px" width="134" height="122" viewBox="0 0 134 122" aria-hidden="true"><path d="M67 6L128 114H6Z" fill="none" stroke="#e6e9ee" stroke-width="6" stroke-linejoin="round"/><rect x="62" y="40" width="10" height="44" rx="4" fill="#e6e9ee"/><circle cx="67" cy="97" r="6" fill="#e6e9ee"/></svg>
  <footer class="footer"><span class="url"><svg width="8" height="8"><use href="#globe"/></svg>kev.org.au</span><span>06</span></footer>
</section>

<!-- Page 7: risks 1-7 -->
<section class="page r3 c1">
  <header class="mini-head"><span class="dot"></span><h2>4.Risks of Orthodontic Treatment<small>(14 Risk Categories)</small></h2></header>
  <ol class="risks" style="top:73px">
    <li><span class="num">1</span><span class="chip"><svg width="10" height="12" style="color:var(--muted)"><use href="#tooth"/></svg></span>Change in Tooth Colour</li>
    <li><span class="num">2</span><span class="chip"><svg width="10" height="12" style="color:var(--muted)"><use href="#tooth"/></svg></span>Tooth Sensitivity</li>
    <li><span class="num">3</span><span class="chip"><svg width="10" height="12" style="color:var(--muted)"><use href="#tooth"/></svg></span>Discomfort</li>
    <li><span class="num">4</span><span class="chip"><svg width="10" height="12" style="color:var(--muted)"><use href="#tooth"/></svg></span>Root Resorption</li>
    <li><span class="num">5</span><span class="chip"><svg width="10" height="12" style="color:var(--muted)"><use href="#tooth"/></svg></span>Decalcification (White Spots)</li>
    <li><span class="num">6</span><span class="chip"><svg width="10" height="12" style="color:var(--muted)"><use href="#tooth"/></svg></span>Gum Problems</li>
    <li><span class="num">7</span><span class="chip"><svg width="10" height="12" style="color:var(--muted)"><use href="#tooth"/></svg></span>Tooth Movement Limitations</li>
  </ol>
  <div class="box" style="top:272px;height:37px;background:#fff;padding:8px 0 0 36px;font-size:5.8px;line-height:1.8">
    <svg style="position:absolute;left:12px;top:9px;color:var(--navy)" width="17" height="17" viewBox="0 0 17 17"><circle cx="8.5" cy="8.5" r="7.5" fill="none" stroke="currentColor"/><rect x="7.8" y="7" width="1.4" height="5" fill="currentColor"/><circle cx="8.5" cy="5" r=".9" fill="currentColor"/></svg>
    Please see the following pages for full explanations<br>of all 14 risk categories.
  </div>
  <footer class="footer"><span class="url"><svg width="8" height="8"><use href="#globe"/></svg>kev.org.au</span><span>07</span></footer>
</section>

<!-- Page 8: risks 8-14 -->
<section class="page r3 c2">
  <header class="mini-head"><span class="dot"></span><h2>4.Risks of Orthodontic Treatment<small>(continued)</small></h2></header>
  <ol class="risks" style="top:73px">
    <li><span class="num">8</span><span class="chip"><svg width="10" height="12" style="color:var(--muted)"><use href="#tooth"/></svg></span>Treatment Duration</li>
    <li><span class="num">9</span><span class="chip"><svg width="10" height="12" style="color:var(--muted)"><use href="#tooth"/></svg></span>Relapse</li>
    <li><span class="num">10</span><span class="chip"><svg width="10" height="12" style="color:var(--muted)"><use href="#tooth"/></svg></span>Changes to Bite</li>
    <li><span class="num">11</span><span class="chip"><svg width="10" height="12" style="color:var(--muted)"><use href="#tooth"/></svg></span>Need for Additional Treatment</li>
    <li><span class="num">12</span><span class="chip"><svg width="10" height="12" style="color:var(--muted)"><use href="#tooth"/></svg></span>Allergic Reactions</li>
    <li><span class="num">13</span><span class="chip"><svg width="10" height="12" style="color:var(--muted)"><use href="#tooth"/></svg></span>Appliance Breakage or Failure</li>
    <li><span class="num">14</span><span class="chip"><svg width="10" height="12" style="color:var(--muted)"><use href="#tooth"/></svg></span>Other Unexpected Risks</li>
  </ol>
  <footer class="footer"><span class="url"><svg width="8" height="8"><use href="#globe"/></svg>kev.org.au</span><span>08</span></footer>
</section>

<!-- Page 9: 4.1 -->
<section class="page r3 c3">
  <div class="brand" style="top:22px"><span class="dot"></span><span>Kestrel Valley<br>Orthodontics</span></div>
  <div class="top-rule" style="top:53px"></div>
  <h2 class="title" style="top:68px;font-size:10.4px">4.1&nbsp;&nbsp;&nbsp;&nbsp;Change in Tooth Colour</h2>
  <h3 class="sub" style="top:98px">What it is</h3>
  <div class="body" style="top:111px;font-size:5.8px">Minor changes in tooth colour may occur during or after treatment due to factors such as staining, decalcification or tooth trauma.</div>
  <h3 class="sub" style="top:148px">How common is it?</h3>
  <div class="body" style="top:161px;font-size:5.8px">Uncommon.</div>
  <h3 class="sub" style="top:188px">Can it be treated?</h3>
  <div class="body" style="top:201px;font-size:5.8px">In most cases, yes. Your orthodontist or dentist can advise on whitening or other treatment options if needed.</div>
  <div class="box" style="top:243px;height:73px;background:#fff;padding:9px 0 0 32px">
    <svg style="position:absolute;left:11px;top:7px" width="16" height="18" viewBox="0 0 16 18"><g fill="none" stroke="var(--navy)" stroke-width="1"><path d="M8 4a4.5 4.5 0 0 0-2.6 8.2V14h5.2v-1.8A4.5 4.5 0 0 0 8 4z"/><path d="M6 16h4M8 0v2M1.5 3l1.4 1.4M14.5 3l-1.4 1.4"/></g></svg>
    <div style="font-size:6.6px;color:var(--navy);margin-bottom:3px">How to reduce this risk</div>
    <ul style="font-size:5.6px;line-height:12.2px;padding-left:10px;color:var(--ink)">
      <li>Maintain good oral hygiene</li>
      <li>Avoid staining foods and drinks</li>
      <li>Attend regular dental check-ups</li>
    </ul>
  </div>
  <footer class="footer"><span class="url"><svg width="8" height="8"><use href="#globe"/></svg>kev.org.au</span><span>09</span></footer>
</section>
</body>
</html>
```